CPA, Management and IT Consulting Redesign Existing Website

We currently have a website that is outdated (www.kelvorant.com). We need a good website developer that can redesign our website. To make this easier I have chosen a few websites that we like the layout or template. Use our exiting website content for this project. Our new logo is attached below. Based on who wins this we will upgrade to a coded website and a content management system (CMS) so we can make changes to the text ourselves in the future.

http://www.marbeckhollis.com/
http://www.quorvelmanagement.com/

Target Market(s)

Government Clients

Industry/Entity Type

Management Consulting

Number of Pages Required

5+ page

Font styles to use
Serif

Requirements
Must have
• Please the following website templates as a guide.
• http://www.marbeckhollis.com/
• http://www.quorvelmanagement.com/
Nice to have
Should not have

```html
<!DOCTYPE html>
<html lang="en">
<head>
<meta charset="utf-8">
<title>Carrow Enterprises, LLC</title>
<link href="https://fonts.googleapis.com/css2?family=Lato:wght@400;700;900&display=swap" rel="stylesheet">
<style>
:root{
  --orange:#f7941d;
  --ink:#1b1b1b;
  --text:#3a3a3a;
  --muted:#6b6b6b;
  --grey-bg:#efefef;
  --line:#d6d6d6;
  --white:#ffffff;
  --navy:#252e44;
  --footer:#111111;
  --social:#2b4f7e;
}
*{box-sizing:border-box;margin:0;padding:0}
html,body{width:1200px;height:2707px;overflow:hidden}
body{font-family:'Lato',Arial,sans-serif;color:var(--text);background:var(--white);position:relative}

/* header */
.site-header{position:absolute;left:0;top:0;width:1200px;height:127px;background:var(--white)}
.brand{position:absolute;left:110px;top:34px;display:flex;align-items:flex-start;gap:16px}
.brand-mark{width:64px;height:64px;background:var(--orange)}
.brand-words{display:flex;flex-direction:column;padding-top:1px}
.brand-name{font-size:40px;font-weight:900;color:var(--ink);line-height:36px;letter-spacing:.5px}
.brand-sub{font-size:22px;font-weight:700;color:var(--orange);line-height:24px;letter-spacing:.3px}
.brand-tag{font-size:8px;color:var(--muted);letter-spacing:1px;line-height:12px;margin-top:2px}
.top-contact{position:absolute;right:110px;top:24px;display:flex;gap:26px;font-size:17px;color:var(--ink)}
.top-contact span{display:flex;align-items:center;gap:10px}
.round-ico{width:28px;height:28px;border-radius:50%;background:var(--orange);display:flex;align-items:center;justify-content:center}
.main-nav{position:absolute;right:100px;top:72px;display:flex;gap:4px}
.main-nav a{font-size:14px;font-weight:700;color:var(--ink);text-decoration:none;padding:8px 17px;border-radius:2px}
.main-nav a.active{background:var(--ink);color:var(--white)}

/* hero */
.hero{position:absolute;left:0;top:127px;width:1200px;height:518px;background:linear-gradient(120deg,#9db8d4 0%,#c9d7e6 35%,#e6d8cc 55%,#5d7fa6 85%,#3d5d85 100%)}
.hero-arrow{position:absolute;top:240px;width:20px;height:40px}
.hero-caption{position:absolute;left:0;bottom:0;width:100%;height:90px;background:rgba(30,30,30,.72);color:var(--white);font-size:26px;text-align:center;line-height:38px;padding-top:8px}

/* section titles */
.section-title{position:absolute;left:0;width:1200px;text-align:center;font-size:28px;font-weight:700;color:var(--ink);letter-spacing:.3px}
.section-title em{font-style:normal;color:var(--orange)}
.title-rule{position:absolute;left:50%;width:530px;margin-left:-265px;height:12px}
.title-rule::before{content:"";position:absolute;left:0;right:0;top:5px;height:1px;background:var(--line)}
.title-rule::after{content:"";position:absolute;left:50%;top:1px;width:8px;height:10px;margin-left:-4px;background:var(--ink);border-left:3px solid var(--white);border-right:3px solid var(--white)}

/* welcome */
.welcome-copy{position:absolute;left:112px;top:764px;width:976px;text-align:center;font-size:15.3px;line-height:23.5px;color:var(--text)}
.btn{display:inline-block;background:var(--orange);color:var(--white);font-weight:700;text-decoration:none;border-radius:2px}
.btn-read{position:absolute;left:543px;top:890px;width:116px;height:35px;line-height:35px;text-align:center;font-size:14px}

/* services */
.services{position:absolute;left:0;top:975px;width:1200px;height:430px;background:var(--grey-bg)}
.service{position:absolute;top:140px;width:254px;text-align:center}
.service + .service{border-left:1px solid var(--line)}
.service svg{height:92px;display:block;margin:0 auto}
.service h3{margin-top:22px;font-size:21px;font-weight:700;color:var(--ink);line-height:27px}
.service.active h3{color:var(--orange);font-weight:400}
.service p{margin-top:16px;font-size:15.5px;line-height:24px;color:var(--text)}
.service p b{font-weight:400;color:var(--orange)}

/* consulting banner */
.consult{position:absolute;left:108px;top:1455px;width:984px;height:312px;background:var(--navy)}
.consult-photo{position:absolute;right:0;top:0;width:320px;height:312px;background:linear-gradient(135deg,#6b7588 0%,#c8b08a 45%,#e6d6b8 60%,#5a6478 100%)}
.consult h2{position:absolute;left:34px;top:58px;font-size:40px;font-weight:400;color:var(--white);letter-spacing:.5px}
.consult p{position:absolute;left:34px;top:116px;font-size:21px;line-height:30px;color:var(--white)}
.btn-contact{position:absolute;left:34px;top:196px;width:224px;height:40px;line-height:40px;text-align:center;font-size:20px;font-weight:400}

/* industries */
.industries{position:absolute;left:0;top:1820px;width:1200px;height:475px;background:var(--grey-bg)}
.ind-card{position:absolute;width:224px;height:146px;background:var(--white);text-align:center;font-size:13px;line-height:17px;color:var(--ink)}
.ind-card .ico{width:58px;height:58px;border-radius:50%;background:#e7e7e7;margin:18px auto 12px;display:flex;align-items:center;justify-content:center}
.ind-hub{position:absolute;left:313px;top:260px;width:46px;height:46px;border-radius:50%;background:var(--grey-bg)}
.video{position:absolute;left:670px;top:128px;width:418px;height:294px;background:linear-gradient(135deg,#cdd6df 0%,#9aa6b4 40%,#3a4658 75%,#c2cad4 100%)}
.video-bar{position:absolute;left:0;bottom:0;width:100%;height:26px;background:#1a1a1a}
.video-play{position:absolute;left:179px;top:104px;width:60px;height:60px;border-radius:50%;background:rgba(20,20,20,.55);border:2px solid var(--white);display:flex;align-items:center;justify-content:center}

/* clients */
.clients-label{position:absolute;left:110px;top:2340px;font-size:28px;font-weight:700;line-height:30px;color:var(--ink)}
.clients-label em{font-style:normal;color:var(--orange)}
.client-badge{position:absolute;top:2342px;width:146px;height:64px;background:var(--white);border:1px solid #e4e4e4}
.client-badge i{position:absolute;left:18px;top:16px;width:108px;height:30px;background:#d9dee6;border-radius:3px}

/* footer */
.site-footer{position:absolute;left:0;top:2457px;width:1200px;height:205px;background:var(--footer);color:var(--white)}
.foot-nav{position:absolute;left:162px;top:32px;display:flex;align-items:center;font-size:13px}
.foot-nav a{color:var(--white);text-decoration:none}
.foot-nav .sep{width:6px;height:6px;margin:0 44px;background:var(--orange);box-shadow:0 0 0 2px var(--footer),0 0 0 3px var(--orange)}
.foot-rule{position:absolute;left:108px;top:86px;width:732px;height:1px;background:#333}
.foot-address{position:absolute;left:108px;top:100px;font-size:13.5px;line-height:20px}
.foot-address b{font-weight:700}
.foot-contact{position:absolute;left:412px;top:100px;font-size:13.5px;line-height:30px}
.foot-contact div{display:flex;align-items:center;gap:12px}
.foot-form{position:absolute;left:646px;top:100px}
.foot-form .field{width:196px;height:32px;border:1px solid var(--white);padding:0 10px;font-size:12px;line-height:30px;color:var(--white)}
.foot-form .submit{margin-top:14px;width:196px;height:32px;line-height:32px;text-align:center;font-size:15px;font-weight:700;background:var(--orange);border-radius:2px}
.foot-mark{position:absolute;left:924px;top:28px;width:144px;height:144px;background:#2c2c2c}
.copy-bar{position:absolute;left:0;top:2662px;width:1200px;height:45px;background:var(--orange)}
.copy-bar p{position:absolute;left:108px;top:14px;font-size:13px;color:var(--white)}
.socials{position:absolute;right:110px;top:8px;display:flex;gap:8px}
.socials span{width:28px;height:28px;border-radius:50%;background:var(--social);border:2px solid var(--white)}
</style>
</head>
<body>

<header class="site-header">
  <div class="brand">
    <div class="brand-mark"></div>
    <div class="brand-words">
      <div class="brand-name">CARROW</div>
      <div class="brand-sub">ENTERPRISES, LLC</div>
      <div class="brand-tag">CONSULTANTS AND CERTIFIED PUBLIC ACCOUNTANTS</div>
    </div>
  </div>
  <div class="top-contact">
    <span><i class="round-ico"><svg width="14" height="14" viewBox="0 0 24 24"><path fill="#fff" d="M6.6 10.8a15 15 0 0 0 6.6 6.6l2.2-2.2c.3-.3.7-.4 1-.2 1.1.4 2.3.6 3.6.6.6 0 1 .4 1 1V20c0 .6-.4 1-1 1A17 17 0 0 1 3 4c0-.6.4-1 1-1h3.5c.6 0 1 .4 1 1 0 1.3.2 2.5.6 3.6.1.3 0 .7-.2 1z"/></svg></i>(202) 555-0148</span>
    <span><i class="round-ico"><svg width="14" height="12" viewBox="0 0 24 18"><path fill="#fff" d="M0 0h24v18H0z"/><path fill="none" stroke="#f7941d" stroke-width="2" d="M1 1l11 9 11-9"/></svg></i>info@kelvorant.com</span>
  </div>
  <nav class="main-nav">
    <a class="active" href="#">HOME</a><a href="#">ABOUT US</a><a href="#">SERVICES</a><a href="#">INDUSTRIES</a><a href="#">CONTACT US</a>
  </nav>
</header>

<section class="hero" role="img" aria-label="Photo of business professionals reviewing financial charts on a tablet with pens">
  <svg class="hero-arrow" style="left:52px" viewBox="0 0 20 40"><path d="M16 4L4 20l12 16" fill="none" stroke="#fff" stroke-width="2.5"/></svg>
  <svg class="hero-arrow" style="right:52px" viewBox="0 0 20 40"><path d="M4 4l12 16L4 36" fill="none" stroke="#fff" stroke-width="2.5"/></svg>
  <div class="hero-caption">We Are Committed To Professional Excellence Across All Service Areas Including Audit<br>&amp; Assurance, Accounting, Tax, Management Consulting, &amp; Information Technology</div>
</section>

<h1 class="section-title" style="top:690px">WELCOME TO CARROW <em>ENTERPRISES, LLC</em></h1>
<div class="title-rule" style="top:731px"></div>
<p class="welcome-copy">Carrow Enterprises, LLC and Bellamy &amp; Shore, LLC is a network of certified public accounting and management consulting firms with seasoned professionals and an excellent reputation for serving a diverse client base including federal agencies, state and local government, non-profit organizations, small and medium-sized business entities, professional associations and individuals. We are committed to professional excellence across all service areas including Audit and Assurance, Accounting, Tax, Management Consulting, and Information Technology.</p>
<a class="btn btn-read" href="#">READ MORE</a>

<section class="services">
  <h2 class="section-title" style="top:38px">OUR <em>SERVICES</em></h2>
  <div class="title-rule" style="top:79px"></div>

  <div class="service active" style="left:100px">
    <svg viewBox="0 0 92 92"><g fill="none" stroke="#f7941d" stroke-width="3"><ellipse cx="30" cy="70" rx="20" ry="6"/><path d="M10 70v10c0 3 9 6 20 6s20-3 20-6V70"/><path d="M10 56v10"/><ellipse cx="30" cy="56" rx="20" ry="6"/><path d="M10 42v14M50 42v14"/><ellipse cx="30" cy="42" rx="20" ry="6"/><circle cx="56" cy="30" r="18"/><path d="M69 43l17 17"/></g></svg>
    <h3>Audit, Accounting<br>&amp; Tax</h3>
    <p>Lorem ipsum dolor sit amet,<br>consectetuer adipis <b>...[+]</b></p>
  </div>
  <div class="service" style="left:346px">
    <svg viewBox="0 0 92 92"><g fill="#1b1b1b"><rect x="6" y="58" width="9" height="24"/><rect x="20" y="50" width="9" height="32"/><rect x="34" y="54" width="9" height="28"/><rect x="48" y="40" width="9" height="42"/><rect x="62" y="30" width="9" height="52"/><rect x="76" y="16" width="9" height="66"/><rect x="2" y="84" width="88" height="3"/></g><path d="M8 48l16-10 14 6 14-14 14-6 18-14" fill="none" stroke="#1b1b1b" stroke-width="3"/><circle cx="84" cy="10" r="4" fill="#1b1b1b"/></svg>
    <h3>Financial<br>Management</h3>
    <p>Lorem ipsum dolor sit amet,<br>consectetuer adipis ...[+]</p>
  </div>
  <div class="service" style="left:600px">
    <svg viewBox="0 0 92 92"><rect x="24" y="4" width="40" height="64" rx="4" fill="none" stroke="#1b1b1b" stroke-width="4"/><rect x="30" y="12" width="28" height="46" fill="#fff"/><path d="M46 50v-14c0-3 5-3 5 0v10l8 2c3 1 5 3 4 7l-3 20H44l-8-12c-2-3 1-6 4-4l6 5z" fill="#1b1b1b"/></svg>
    <h3>Information<br>Technology</h3>
    <p>Lorem ipsum dolor sit amet,<br>consectetuer adipis ...[+]</p>
  </div>
  <div class="service" style="left:854px">
    <svg viewBox="0 0 92 92"><g fill="#1b1b1b"><circle cx="46" cy="12" r="8"/><path d="M32 34c0-10 28-10 28 0z"/><circle cx="16" cy="60" r="8"/><path d="M2 82c0-10 28-10 28 0z"/><circle cx="76" cy="60" r="8"/><path d="M62 82c0-10 28-10 28 0z"/></g><path d="M46 38v12M46 50L22 56M46 50l24 6" fill="none" stroke="#1b1b1b" stroke-width="2" stroke-dasharray="3 3"/></svg>
    <h3>Governance, Risk<br>&amp; Compliance</h3>
    <p>Lorem ipsum dolor sit amet,<br>consectetuer adipis ...[+]</p>
  </div>
</section>

<section class="consult">
  <div class="consult-photo" role="img" aria-label="Overhead photo of a team meeting around a conference table with laptops"></div>
  <h2>CONSULTING SERVICE</h2>
  <p>We Are Providing Wide Range Of Consulting Services<br>&amp; World Wide Happy Clients</p>
  <a class="btn btn-contact" href="#">CONTACT US TODAY</a>
</section>

<section class="industries">
  <h2 class="section-title" style="top:36px">INDUSTRIES WE <em>WORK WITH</em></h2>
  <div class="title-rule" style="top:77px"></div>

  <div class="ind-card" style="left:108px;top:125px">
    <div class="ico"><svg width="32" height="30" viewBox="0 0 32 30"><path d="M16 1L1 9h30z" fill="#1b1b1b"/><g fill="#1b1b1b"><rect x="4" y="11" width="3" height="13"/><rect x="10" y="11" width="3" height="13"/><rect x="19" y="11" width="3" height="13"/><rect x="25" y="11" width="3" height="13"/><rect x="1" y="25" width="30" height="4"/></g></svg></div>
    FEDERAL<br>GOVERNMENT
  </div>
  <div class="ind-card" style="left:345px;top:125px">
    <div class="ico"><svg width="32" height="32" viewBox="0 0 32 32"><g fill="#1b1b1b"><rect x="15" y="0" width="2" height="5"/><path d="M7 13c0-6 18-6 18 0z"/><rect x="6" y="14" width="20" height="2"/><rect x="8" y="17" width="3" height="9"/><rect x="14.5" y="17" width="3" height="9"/><rect x="21" y="17" width="3" height="9"/><rect x="3" y="27" width="26" height="4"/></g></svg></div>
    STATE &amp; LOCAL<br>GOVERNMENT
  </div>
  <div class="ind-card" style="left:108px;top:282px">
    <div class="ico"><svg width="32" height="30" viewBox="0 0 32 30"><g fill="#1b1b1b"><rect x="8" y="2" width="22" height="14" rx="1"/><rect x="4" y="8" width="22" height="14" rx="1" stroke="#e7e7e7" stroke-width="1.5"/><ellipse cx="8" cy="26" rx="7" ry="3"/></g><text x="15" y="19" fill="#e7e7e7" font-size="10" font-family="Lato,sans-serif" font-weight="700" text-anchor="middle">$</text></svg></div>
    FINANCIAL<br>SERVICES
  </div>
  <div class="ind-card" style="left:345px;top:282px">
    <div class="ico"><svg width="34" height="26" viewBox="0 0 34 26"><path d="M1 6l7-4 6 3 5-3 6 1 8 5-6 10-5 5c-2 2-4 0-3-1l-3 2c-2 1-3-1-2-2l-3 1c-2 0-2-2-1-3l-2 1c-2 0-2-2-1-3L3 13z" fill="#1b1b1b"/></svg></div>
    NOT-FOR<br>PROFIT
  </div>
  <div class="ind-hub"></div>

  <div class="video" role="img" aria-label="Video still of a business team meeting in an office">
    <div class="video-play"><svg width="24" height="26" viewBox="0 0 24 26"><path d="M5 2l17 11L5 24z" fill="#fff"/></svg></div>
    <div class="video-bar"><svg width="418" height="26" viewBox="0 0 418 26"><rect x="10" y="8" width="3" height="10" fill="#fff"/><rect x="16" y="8" width="3" height="10" fill="#fff"/><rect x="32" y="12" width="260" height="3" fill="#555"/><rect x="32" y="12" width="140" height="3" fill="#3a8ee6"/><circle cx="172" cy="13" r="5" fill="#fff"/><rect x="320" y="9" width="10" height="9" fill="#888"/><rect x="345" y="12" width="50" height="3" fill="#666"/><circle cx="372" cy="13" r="7" fill="#fff"/></svg></div>
  </div>
</section>

<div class="clients-label">OUR<br><em>CLIENTS</em></div>
<div class="client-badge" style="left:256px" role="img" aria-label="Contract vehicle badge"><i></i></div>
<div class="client-badge" style="left:480px" role="img" aria-label="Schedule contract badge"><i></i></div>
<div class="client-badge" style="left:706px" role="img" aria-label="Small business certification badge"><i></i></div>
<div class="client-badge" style="left:932px" role="img" aria-label="Professional association badge"><i></i></div>

<footer class="site-footer">
  <nav class="foot-nav">
    <a href="#">HOME</a><span class="sep"></span><a href="#">ABOUT US</a><span class="sep"></span><a href="#">SERVICES</a><span class="sep"></span><a href="#">INDUSTRIES</a><span class="sep"></span><a href="#">CONTACT US</a>
  </nav>
  <div class="foot-rule"></div>
  <div class="foot-address"><b>CARROW ENTERPRISES, LLC</b><br>418 Larkin Street NW,<br>Suite 300 Washington,<br>DC 20009</div>
  <div class="foot-contact">
    <div><svg width="14" height="14" viewBox="0 0 24 24"><path fill="#f7941d" d="M6.6 10.8a15 15 0 0 0 6.6 6.6l2.2-2.2c.3-.3.7-.4 1-.2 1.1.4 2.3.6 3.6.6.6 0 1 .4 1 1V20c0 .6-.4 1-1 1A17 17 0 0 1 3 4c0-.6.4-1 1-1h3.5c.6 0 1 .4 1 1 0 1.3.2 2.5.6 3.6.1.3 0 .7-.2 1z"/></svg>(202) 555-0148</div>
    <div><svg width="14" height="14" viewBox="0 0 24 24"><g fill="#f7941d"><rect x="6" y="2" width="12" height="6"/><rect x="2" y="9" width="20" height="9" rx="2"/><rect x="6" y="15" width="12" height="7"/></g></svg>(202) 555-0173</div>
    <div><svg width="14" height="11" viewBox="0 0 24 18"><path fill="#f7941d" d="M0 0h24v18H0z"/><path fill="none" stroke="#111" stroke-width="2" d="M1 1l11 9 11-9"/></svg>info@kelvorant.com</div>
  </div>
  <div class="foot-form">
    <div class="field">Enter Your Email Here</div>
    <div class="submit">SUBMIT</div>
  </div>
  <div class="foot-mark"></div>
</footer>

<div class="copy-bar">
  <p>Copyright © 2016 Carrow Enterprises, LLC. All Rights Reserved.</p>
  <div class="socials" aria-label="Social links"><span></span><span></span><span></span><span></span></div>
</div>

</body>
</html>
```